insurance federation
Türkiye Poliçe Aracıları Birliği Konfederasyonu
Project: insurance federation
insurance federation - Financial Services
Creative Brief
Professional
Lale Meydanı Ihlamur Caddesi No:72-B/3 Çamlıtepe – Ankara / TÜRKİYE
info@pabik.org.tr
www.pabik.org.tr
please use logo (like a shadow)

```html
<!DOCTYPE html>
<html lang="tr">
<head>
<meta charset="utf-8">
<title>PABİK – Kurumsal Kırtasiye</title>
<link href="https://fonts.googleapis.com/css2?family=Open+Sans:wght@400;600&display=swap" rel="stylesheet">
<style>
:root{
  --bg:#eeeeef;
  --paper:#ffffff;
  --red:#8e1e29;
  --rule:#c9c9cb;
  --ink:#4d4d4f;
  --ink-soft:#8a8a8c;
}
*{margin:0;padding:0;box-sizing:border-box}
html,body{width:1200px;height:937px;overflow:hidden;background:var(--bg)}
body{position:relative;font-family:"Open Sans",Arial,sans-serif;color:var(--ink)}
.sheet{position:absolute;background:var(--paper);box-shadow:0 2px 6px rgba(0,0,0,.18);overflow:hidden}
.band{position:absolute;left:0;bottom:0;width:100%}
.brand{display:flex;align-items:center;position:absolute}
.brand-square{background:var(--red);flex:none}
.brand-name{font-family:"Open Sans",Arial,sans-serif;font-weight:600;color:var(--ink);letter-spacing:.06em;line-height:1}
.brand-tag{font-family:"Open Sans",Arial,sans-serif;font-weight:400;color:var(--ink-soft);line-height:1.2}
.white{color:#fff}

/* letterhead */
.letterhead{left:182px;top:68px;width:395px;height:572px}
.letterhead .brand{left:22px;top:28px;gap:7px}
.letterhead .brand-square{width:14px;height:14px}
.letterhead .brand-name{font-size:17px}
.letter-body{position:absolute;left:24px;top:88px;width:290px;font-size:4.6px;line-height:1.55;color:var(--ink-soft)}
.letter-body p{margin-bottom:6px}
.signature{width:30px;height:10px;background:#555;opacity:.35;border-radius:2px;margin:6px 0 4px}
.letter-contact{position:absolute;right:14px;bottom:18px;text-align:right;font-size:4.8px;line-height:1.7}

/* folder */
.folder{left:638px;top:40px;width:450px;height:600px}
.folder .brand{left:70px;top:250px;gap:16px}
.folder .brand-square{width:44px;height:44px}
.folder .brand-name{font-size:48px}
.folder .brand-tag{position:absolute;left:130px;top:306px;font-size:9.5px}
.folder-url{position:absolute;right:28px;bottom:18px;font-size:9px;letter-spacing:.28em}

/* cards */
.card-front{left:46px;top:668px;width:144px;height:86px}
.card-front .brand{left:8px;top:10px;gap:4px}
.card-front .brand-square{width:8px;height:8px}
.card-front .brand-name{font-size:10px}
.card-person{position:absolute;left:8px;top:30px;font-size:3.8px;line-height:1.5;color:var(--red)}
.card-contact{position:absolute;right:8px;bottom:8px;text-align:right;font-size:3.6px;line-height:1.55;color:var(--ink-soft)}
.card-back{left:46px;top:779px;width:144px;height:89px}
.card-back .brand{left:12px;top:37px;gap:5px}
.card-back .brand-square{width:10px;height:10px}
.card-back .brand-name{font-size:13px}

/* envelopes */
.envelope{left:261px;top:670px;width:435px;height:198px}
.envelope .brand{left:14px;top:16px;gap:6px}
.envelope .brand-square{width:12px;height:12px}
.envelope .brand-name{font-size:15px}
.envelope .brand-tag{position:absolute;left:32px;top:34px;font-size:5px}
.envelope-url{position:absolute;right:22px;bottom:12px;font-size:7px;letter-spacing:.25em}
.envelope-back{left:734px;top:670px;width:425px;height:198px}
.flap{position:absolute;left:0;top:0;width:100%}
.flap-url{position:absolute;left:0;right:0;top:22px;text-align:center;font-size:8px;letter-spacing:.3em}
</style>
</head>
<body>

<section class="sheet letterhead">
  <div class="brand"><span class="brand-square"></span><span class="brand-name">PABİK</span></div>
  <div class="letter-body">
    <p>12 Mart 2024<br>Sayın Ad Soyad<br>Kurum Adı, Cadde No:1 – Ankara</p>
    <p>Federasyonumuzun yıllık toplantısı bu ay düzenlenecektir. Üyelerimizin görüş ve önerilerini paylaşması, sektörün geleceği açısından büyük önem taşımaktadır. Katılımınız için şimdiden teşekkür ederiz.</p>
    <p>Toplantıda sigorta aracılığı mevzuatı, dijital dönüşüm ve eğitim programları ele alınacaktır. Gündem ve katılım formu ekte yer almaktadır. Sorularınız için sekreterliğimize ulaşabilirsiniz.</p>
    <p>Ortak hedeflerimize birlikte ulaşmak dileğiyle, iş birliğinizin devamını temenni ederiz.</p>
    <p>Saygılarımızla,</p>
    <div class="signature" role="img" aria-label="Handwritten signature"></div>
    <p>Ad Soyad<br>Genel Sekreter</p>
  </div>
  <svg class="band" width="395" height="110" viewBox="0 0 100 100" preserveAspectRatio="none" aria-hidden="true">
    <line x1="0" y1="30" x2="100" y2="30" stroke="var(--rule)" stroke-width="1" vector-effect="non-scaling-stroke"/>
    <path d="M0,60 Q50,40 100,38 L100,100 L0,100Z" fill="var(--red)"/>
  </svg>
  <div class="letter-contact white">
    Lale Meydanı Ihlamur Caddesi No:72-B/3 Çamlıtepe<br>
    Ankara / TÜRKİYE<br>
    +90 312 555 01 49<br>
    info@pabik.org.tr<br>
    www.pabik.org.tr
  </div>
</section>

<section class="sheet folder">
  <div class="brand"><span class="brand-square"></span><span class="brand-name">PABİK</span></div>
  <div class="brand-tag">Türkiye Poliçe Aracıları Birliği Konfederasyonu</div>
  <svg class="band" width="450" height="130" viewBox="0 0 100 100" preserveAspectRatio="none" aria-hidden="true">
    <line x1="0" y1="28" x2="100" y2="28" stroke="var(--rule)" stroke-width="1" vector-effect="non-scaling-stroke"/>
    <path d="M0,58 Q50,40 100,38 L100,100 L0,100Z" fill="var(--red)"/>
  </svg>
  <div class="folder-url white">www.pabik.org.tr</div>
</section>

<section class="sheet card-front">
  <div class="brand"><span class="brand-square"></span><span class="brand-name">PABİK</span></div>
  <div class="card-person"><strong>Ad Soyad</strong><br>Genel Sekreter</div>
  <div class="card-contact">
    +90 312 555 01 49<br>
    info@pabik.org.tr<br>
    Lale Meydanı Ihlamur Cad. No:72-B/3<br>
    Çamlıtepe – Ankara
  </div>
</section>

<section class="sheet card-back">
  <div class="brand"><span class="brand-square"></span><span class="brand-name">PABİK</span></div>
</section>

<section class="sheet envelope">
  <div class="brand"><span class="brand-square"></span><span class="brand-name">PABİK</span></div>
  <div class="brand-tag">Türkiye Poliçe Aracıları Birliği Konfederasyonu</div>
  <svg class="band" width="435" height="110" viewBox="0 0 100 100" preserveAspectRatio="none" aria-hidden="true">
    <line x1="0" y1="24" x2="100" y2="24" stroke="var(--rule)" stroke-width="1" vector-effect="non-scaling-stroke"/>
    <path d="M0,58 Q50,38 100,36 L100,100 L0,100Z" fill="var(--red)"/>
  </svg>
  <div class="envelope-url white">www.pabik.org.tr</div>
</section>

<section class="sheet envelope-back">
  <svg class="flap" width="425" height="70" viewBox="0 0 100 100" preserveAspectRatio="none" aria-hidden="true">
    <path d="M0,0 L100,0 L100,35 L50,100 L0,35Z" fill="var(--red)"/>
  </svg>
  <div class="flap-url white">www.pabik.org.tr</div>
</section>

</body>
</html>
```